Simple and Clean business card design

We would like the design to be simple clean and to incorporate our colors.

We are open to your design and talent, we have the dots in our logo as we think of it as data points and we connect data points for people.

We are open to see the great creative and clean design you bring to the table

Contact Information for Business Card

please include: name, position, email, phone and website

Font styles to use
Sans Serif

Requirements
Must have
• my colors incorporated, simplicity
Nice to have
• lots of white space, simplicity
Should not have
• complexicity/ complex art

```html
<!DOCTYPE html>
<html lang="en">
<head>
<meta charset="utf-8">
<title>Nodera Business Card</title>
<link rel="stylesheet" href="https://fonts.googleapis.com/css2?family=Open+Sans:wght@400;600&family=Rubik:wght@600&display=swap">
<style>
  :root {
    --brand-blue: #4485f4;
    --ink: #1b1b1b;
    --paper: #ffffff;
    --backdrop: #fdfdfd;
    --card-border: #333333;
  }
  * { box-sizing: border-box; margin: 0; padding: 0; }
  html, body {
    width: 1200px; height: 1200px; overflow: hidden;
    background: var(--backdrop);
    font-family: "Open Sans", Arial, sans-serif;
  }
  .canvas { position: relative; width: 1200px; height: 1200px; }
  .card { position: absolute; top: 215px; width: 428px; height: 770px; }
  .card--back { left: 147px; background: var(--brand-blue); }
  .card--front { left: 625px; background: var(--paper); border: 1px solid var(--card-border); }

  .wordmark {
    position: absolute; left: 0; right: 0;
    display: flex; align-items: center; justify-content: center; gap: 10px;
    font-family: "Open Sans", Arial, sans-serif; font-weight: 600;
    line-height: 1; letter-spacing: 1px;
  }
  .wordmark__dot { width: 22px; height: 22px; border-radius: 50%; }
  .card--back .wordmark { top: 582px; font-size: 84px; color: var(--paper); }
  .card--back .wordmark__dot { background: var(--paper); }
  .card--front .wordmark { top: 160px; font-size: 92px; color: var(--ink); }
  .card--front .wordmark__dot { background: var(--brand-blue); }

  .back-url {
    position: absolute; left: 0; right: 0; top: 722px;
    text-align: center; color: var(--paper); font-size: 18px;
  }

  .person { position: absolute; left: 0; right: 0; top: 442px; text-align: center; }
  .person__name {
    font-family: "Rubik", Arial, sans-serif; font-weight: 600;
    font-size: 46px; color: var(--brand-blue); letter-spacing: 2px; line-height: 1;
  }
  .person__role {
    margin-top: 8px; font-family: "Rubik", Arial, sans-serif; font-weight: 600;
    font-size: 21px; color: var(--ink); letter-spacing: 3px; line-height: 1;
  }

  .icon-row {
    position: absolute; left: 0; right: 0; top: 535px;
    display: flex; align-items: center; justify-content: center; gap: 10px;
  }
  .icon-row__rule { width: 47px; height: 2px; background: var(--brand-blue); margin: 0 12px; }
  .icon-tile {
    width: 43px; height: 42px; border: 2.5px solid var(--ink); border-radius: 8px;
    padding: 2px; background: var(--paper);
  }
  .icon-tile__inner {
    width: 100%; height: 100%; border-radius: 5px; background: var(--brand-blue);
    display: flex; align-items: center; justify-content: center;
  }

  .contact {
    position: absolute; left: 0; right: 0; top: 597px;
    list-style: none; text-align: center; color: var(--ink);
    font-size: 21px; line-height: 31.5px;
  }
  .divider {
    position: absolute; left: 60px; right: 62px; top: 706px; height: 2px;
    background: linear-gradient(90deg, rgba(0,0,0,0), #333 50%, rgba(0,0,0,0));
  }
  .address {
    position: absolute; left: 0; right: 0; top: 722px;
    text-align: center; color: var(--ink); font-size: 18px;
  }
</style>
</head>
<body>
<main class="canvas">
  <section class="card card--back">
    <div class="wordmark"><span class="wordmark__dot"></span><span>Nodera</span></div>
    <p class="back-url">www.nodera.io</p>
  </section>

  <section class="card card--front">
    <div class="wordmark"><span class="wordmark__dot"></span><span>Nodera</span></div>

    <div class="person">
      <h1 class="person__name">DANIEL MOSS</h1>
      <p class="person__role">FOUNDER</p>
    </div>

    <div class="icon-row">
      <span class="icon-row__rule"></span>
      <span class="icon-tile"><span class="icon-tile__inner">
        <svg width="16" height="24" viewBox="0 0 16 24" aria-label="Phone"><rect x="2" y="1" width="12" height="22" rx="2" fill="none" stroke="#fff" stroke-width="1.5"/><circle cx="8" cy="20" r="1" fill="#fff"/></svg>
      </span></span>
      <span class="icon-tile"><span class="icon-tile__inner">
        <svg width="22" height="22" viewBox="0 0 22 22" aria-label="Website"><g fill="none" stroke="#fff" stroke-width="1.2"><circle cx="11" cy="11" r="9"/><ellipse cx="11" cy="11" rx="4" ry="9"/><line x1="2" y1="11" x2="20" y2="11"/><line x1="11" y1="2" x2="11" y2="20"/><line x1="4" y1="6.5" x2="18" y2="6.5"/><line x1="4" y1="15.5" x2="18" y2="15.5"/></g></svg>
      </span></span>
      <span class="icon-tile"><span class="icon-tile__inner">
        <svg width="24" height="18" viewBox="0 0 24 18" aria-label="Email"><g fill="none" stroke="#fff" stroke-width="1.4"><rect x="1" y="2" width="22" height="14"/><polyline points="1,2 12,10 23,2"/><line x1="1" y1="16" x2="9" y2="8"/><line x1="23" y1="16" x2="15" y2="8"/></g></svg>
      </span></span>
      <span class="icon-row__rule"></span>
    </div>

    <ul class="contact">
      <li class="contact__phone">555-014-2298</li>
      <li class="contact__web">www.nodera.io</li>
      <li class="contact__email">daniel.moss@nodera.io</li>
    </ul>

    <div class="divider"></div>
    <p class="address">Address line goes here</p>
  </section>
</main>
</body>
</html>
```